VERIDAX Need a luxury modern business card designed.

Need a luxury modern business card designed. refer to the uploaded files for the company name and logo in the zip file under source files. i will making my descion on monday. so please send in before then so if we need to edit we will have the time. we have a trade show coming up and im on a deadline for printer.

Target Market(s)

high end clients

Contact Information for Business Card

Company nAme and logo. Calvin Ostrow Co-Founder / Project Manager Office # 416-555-0193 Cell # 416-555-0147 VERIDAX.CA Calvin@veridax.ca

Font styles to use
Other font styles liked:
• Modern

Requirements
Must have
• Company name and logo, contact info, using the black, gold and white color scheme.

```html
<!DOCTYPE html>
<html lang="en">
<head>
<meta charset="utf-8">
<title>VERIDAX — Business Card</title>
<link href="https://fonts.googleapis.com/css2?family=Arimo:wght@400&display=swap" rel="stylesheet">
<style>
  :root {
    --page-bg: #1f1f1f;
    --card-bg: #333333;
    --card-bg-deep: #262626;
    --gold: #a8976a;
    --white: #ffffff;
    --text: #ececec;
    --rule: #8d8d8d;
  }
  * { margin: 0; padding: 0; box-sizing: border-box; }
  html, body {
    width: 1200px; height: 895px; overflow: hidden;
    background: var(--page-bg);
    font-family: "Arimo", Arial, sans-serif;
  }
  .sheet {
    width: 1200px; height: 895px;
    display: flex; flex-direction: column;
    align-items: center; justify-content: center; gap: 44px;
  }
  .card {
    width: 620px; height: 354px;
    position: relative; overflow: hidden;
    background: var(--card-bg);
  }

  /* Back side */
  .card-back {
    background: linear-gradient(200deg, #363636 0%, #2f2f2f 55%, var(--card-bg-deep) 100%);
  }
  .back-texture {
    position: absolute; inset: 0;
    background: linear-gradient(160deg, rgba(255,255,255,0.04) 0%, rgba(255,255,255,0) 60%, rgba(168,151,106,0.05) 100%);
  }
  .back-wordmark {
    position: absolute; left: 0; right: 0; top: 50%;
    transform: translateY(-50%);
    text-align: center;
    color: var(--white);
    font-size: 30px; letter-spacing: 10px;
    padding-left: 10px;
  }

  /* Front side */
  .card-front {
    border-bottom: 5px solid var(--gold);
  }
  .brand {
    position: absolute; left: 58px; top: 150px;
    width: 250px;
    display: flex; align-items: center; gap: 14px;
  }
  .brand-square {
    width: 14px; height: 14px; background: var(--gold); flex: none;
  }
  .brand-name {
    color: var(--white);
    font-size: 36px; letter-spacing: 7px;
  }
  .divider {
    position: absolute; left: 345px; top: 56px;
    width: 1px; height: 236px; background: var(--rule);
  }
  .details {
    position: absolute; left: 372px; top: 62px;
    color: var(--text);
  }
  .person-name {
    font-size: 23px; letter-spacing: 1px; color: var(--white); line-height: 1;
  }
  .person-name .surname { color: var(--gold); }
  .person-role { font-size: 14px; margin-top: 5px; }
  .address { font-size: 14px; line-height: 1.35; margin-top: 18px; }
  .contact-list { list-style: none; margin-top: 18px; }
  .contact-list li {
    display: flex; align-items: center; gap: 10px;
    font-size: 14px; line-height: 1; margin-bottom: 9px;
  }
  .contact-label { color: var(--gold); width: 44px; }
  .contact-icon { width: 13px; height: 13px; flex: none; }
</style>
</head>
<body>
  <main class="sheet">
    <section class="card card-back" aria-label="Card back">
      <div class="back-texture" role="img" aria-label="Faint tonal pattern across the dark card back"></div>
      <div class="back-wordmark">VERIDAX</div>
    </section>

    <section class="card card-front" aria-label="Card front">
      <div class="brand">
        <span class="brand-square"></span>
        <span class="brand-name">VERIDAX</span>
      </div>

      <div class="divider"></div>

      <div class="details">
        <p class="person-name">CALVIN <span class="surname">OSTROW</span></p>
        <p class="person-role">Co-Founder / Project Manager</p>
        <p class="address">88 Larkfield Road, Unit 5<br>Ashby, ON. L0X 2B7</p>
        <ul class="contact-list">
          <li>
            <svg class="contact-icon" viewBox="0 0 16 16" aria-hidden="true"><path fill="var(--gold)" d="M3.6 1.2l2.3 2.4-1.3 1.9c.8 2.1 2.6 3.9 4.7 4.8l1.9-1.3 2.4 2.3-1.5 2.4C6.7 13.4 2.6 9.3 1.3 3z"/></svg>
            <span class="contact-label">Office</span>416-555-0193
          </li>
          <li>
            <svg class="contact-icon" viewBox="0 0 16 16" aria-hidden="true"><path fill="var(--gold)" d="M3.6 1.2l2.3 2.4-1.3 1.9c.8 2.1 2.6 3.9 4.7 4.8l1.9-1.3 2.4 2.3-1.5 2.4C6.7 13.4 2.6 9.3 1.3 3z"/></svg>
            <span class="contact-label">Cell</span>416-555-0147
          </li>
          <li>
            <svg class="contact-icon" viewBox="0 0 16 16" aria-hidden="true"><rect x="1.5" y="3.5" width="13" height="9" fill="none" stroke="var(--gold)" stroke-width="1.4"/><path d="M1.5 3.5L8 9l6.5-5.5" fill="none" stroke="var(--gold)" stroke-width="1.4"/></svg>
            Calvin@veridax.ca
          </li>
          <li>
            <svg class="contact-icon" viewBox="0 0 16 16" aria-hidden="true"><g fill="none" stroke="var(--gold)" stroke-width="1.2"><circle cx="8" cy="8" r="6.5"/><ellipse cx="8" cy="8" rx="3" ry="6.5"/><path d="M1.5 8h13M2.5 4.8h11M2.5 11.2h11"/></g></svg>
            VERIDAX.CA
          </li>
        </ul>
      </div>
    </section>
  </main>
</body>
</html>
```